Wattlegrove Campus Lodgings needs a business card design

Hi Guys,

We are a Student Accommodation company in Australia. We already have a logo which I will submit.

I will require the design of the business cards from you.

I am after something that looks clean, modern and that people feel interested and actually want to contact us.

We would like to see designs that are innovative.

On the business cards I will require to have:

Employee Name
Position
Phone number
Email
Facebook page

I hope you can help me with this project guys as I have heard really good things from you.

```html
<!DOCTYPE html>
<html lang="en">
<head>
<meta charset="utf-8">
<title>Wattlegrove Campus Lodgings – Business Card</title>
<link href="https://fonts.googleapis.com/css2?family=Jura:wght@500;700&display=swap" rel="stylesheet">
<style>
  :root {
    --stage: #e4e2df;
    --card: #f3f1ee;
    --ink: #2f2f33;
    --ink-soft: #45454a;
    --green: #14941e;
    --gold: #f3b418;
    --rule: #8c8a90;
    --white: #ffffff;
  }
  * { margin: 0; padding: 0; box-sizing: border-box; }
  html, body { width: 1200px; height: 768px; overflow: hidden; background: var(--stage); }
  body { position: relative; font-family: "Jura", sans-serif; color: var(--ink); }

  .card {
    position: absolute; left: 100px; top: 94px; width: 1000px; height: 580px;
    background: var(--card); border-radius: 30px; overflow: hidden;
    box-shadow: 0 10px 30px rgba(0,0,0,.12);
  }

  .brand { position: absolute; left: 582px; top: 70px; display: flex; align-items: flex-start; gap: 16px; }
  .brand-mark { width: 26px; height: 26px; background: var(--gold); margin-top: 8px; }
  .brand-name {
    font-weight: 700; font-size: 34px; line-height: 1.12; color: var(--green);
    text-transform: uppercase; letter-spacing: 1px;
  }

  .person { position: absolute; left: 38px; top: 180px; }
  .person-name { font-weight: 700; font-size: 30px; letter-spacing: 1.5px; text-transform: uppercase; }
  .person-role { font-weight: 700; font-size: 22px; margin-top: 18px; color: var(--ink-soft); }

  .divider {
    position: absolute; left: 38px; top: 289px; width: 892px; height: 2px;
    background: linear-gradient(90deg, rgba(140,138,144,0), var(--rule) 15%, var(--rule) 85%, rgba(140,138,144,0));
  }

  .address { position: absolute; left: 38px; top: 378px; font-weight: 700; font-size: 23px; line-height: 1.4; color: var(--ink-soft); }

  .contact { position: absolute; right: 40px; top: 312px; list-style: none; text-align: right; }
  .contact li { display: flex; justify-content: flex-end; align-items: center; gap: 14px; font-weight: 700; }
  .contact .tel { font-size: 21px; letter-spacing: 2px; height: 48px; }
  .contact .web { font-size: 19px; height: 34px; }
  .contact svg { width: 22px; height: 22px; fill: none; stroke: var(--ink); stroke-width: 2; }

  .footer-band { position: absolute; left: 0; bottom: 0; width: 1000px; height: 60px; }
  .footer-url {
    position: absolute; left: 38px; top: 548px; font-weight: 700; font-size: 19px;
    color: var(--white); letter-spacing: .5px;
  }
</style>
</head>
<body>
  <div class="card">
    <div class="brand">
      <span class="brand-mark"></span>
      <p class="brand-name">Wattlegrove<br>Campus<br>Lodgings</p>
    </div>

    <div class="person">
      <h1 class="person-name">Liam Hartwell</h1>
      <p class="person-role">Managing Director</p>
    </div>

    <div class="divider"></div>

    <p class="address">Level 4, 12 Acacia Lane<br>Brookvale NSW</p>

    <ul class="contact">
      <li class="tel">013 456 7890
        <svg viewBox="0 0 24 24"><path d="M5 3h4l2 5-2.5 1.5a11 11 0 0 0 6 6L16 13l5 2v4a2 2 0 0 1-2 2A16 16 0 0 1 3 5a2 2 0 0 1 2-2z"/></svg>
      </li>
      <li class="tel">013 456 7891
        <svg viewBox="0 0 24 24"><rect x="6" y="2" width="12" height="20" rx="2"/><line x1="10" y1="18" x2="14" y2="18"/></svg>
      </li>
      <li class="tel">013 456 7892
        <svg viewBox="0 0 24 24"><rect x="3" y="9" width="18" height="12" rx="1"/><rect x="7" y="3" width="10" height="6"/><line x1="7" y1="14" x2="17" y2="14"/><line x1="7" y1="17" x2="13" y2="17"/></svg>
      </li>
      <li class="web">hello@wattlegrove.au
        <svg viewBox="0 0 24 24"><rect x="2" y="5" width="20" height="14"/><polyline points="2,5 12,13 22,5"/></svg>
      </li>
      <li class="web">www.wattlegrove.au
        <svg viewBox="0 0 24 24"><circle cx="12" cy="12" r="10"/><ellipse cx="12" cy="12" rx="4" ry="10"/><line x1="2" y1="12" x2="22" y2="12"/></svg>
      </li>
    </ul>

    <svg class="footer-band" viewBox="0 0 1000 60" preserveAspectRatio="none">
      <path d="M402 19 H1000 V60 H402 Z" fill="var(--green)"/>
      <path d="M0 0 H375 Q400 0 412 25 L428 60 H0 Z" fill="var(--gold)"/>
    </svg>
    <p class="footer-url">www.wattlegrove.au</p>
  </div>
</body>
</html>
```